Open Sky Living newsletter - Mail Chimp

Open Sky Living - Empowering Life Coach needs Mail Chimp Newsletter Template. This is a newsletter I will send out monthly to current clients and prospective clients to offer (hopefully) inspiring and uplifting content AND to give info and dates of my upcoming workshops and retreats.

I have attached a word document with all of the different sections of the mail chimp template I would like to have - and hte actual content for the first newsletter.

I'd like to look uplifting, fun, inspiring.

I also need it to be easy for me to use to update in the future :)

Target Market(s)

Women - moms

Industry/Entity Type

Life Coaching

Requirements
Nice to have
• Color theme to match my "Open Sky Living" logo

```html
<!DOCTYPE html>
<html lang="en">
<head>
<meta charset="utf-8">
<title>Open Sky Living – Monthly Newsletter</title>
<link rel="stylesheet" href="https://fonts.googleapis.com/css2?family=Lora:wght@400;700&family=Open+Sans:wght@400;600&display=swap">
<style>
  :root {
    --navy: #1f2a3c;
    --orange: #e8861e;
    --orange-light: #f5a742;
    --sun: #f7c266;
    --ink: #3a3a3a;
    --muted: #c9ced6;
    --white: #ffffff;
  }
  * { margin: 0; padding: 0; box-sizing: border-box; }
  html, body { width: 1200px; height: 4624px; overflow: hidden; }
  body {
    position: relative;
    background: var(--white);
    font-family: "Open Sans", Arial, sans-serif;
    color: var(--ink);
    font-size: 16px;
    line-height: 28px;
  }
  .abs { position: absolute; }

  /* header */
  .brand { left: 80px; top: 50px; display: flex; align-items: center; gap: 16px; }
  .brand-dot { width: 44px; height: 44px; border-radius: 50%; background: var(--orange); }
  .brand-name { font-family: "Lora", Georgia, serif; font-weight: 700; font-size: 40px; color: var(--navy); line-height: 1; }
  .contact { right: 70px; top: 36px; display: flex; align-items: center; gap: 14px; font-size: 22px; color: var(--navy); }

  /* hero */
  .hero-photo {
    left: 0; top: 140px; width: 1200px; height: 1000px;
    background: radial-gradient(circle at 52% 42%, #fff3c4 0%, var(--sun) 18%, var(--orange-light) 42%, #b9581a 80%, #6d3414 100%);
  }
  .hero-shapes { left: 0; top: 0; }

  /* welcome */
  .portrait {
    left: 60px; top: 1260px; width: 320px; height: 320px; border-radius: 50%;
    border: 8px solid var(--white);
    background: linear-gradient(150deg, #6fa7d6 0%, #2c5d93 55%, #b98662 100%);
  }
  .welcome { left: 640px; top: 1160px; width: 520px; text-align: right; color: var(--muted); font-size: 16px; line-height: 28px; }
  .welcome h1 { font-family: "Lora", Georgia, serif; font-weight: 400; font-size: 38px; color: var(--orange); line-height: 60px; margin-bottom: 24px; }
  .welcome p { margin-bottom: 26px; }
  .welcome .signoff { font-family: "Lora", Georgia, serif; font-size: 30px; color: var(--orange); margin-top: 6px; }

  /* content */
  .content { left: 60px; width: 1100px; }
  .section-title { font-family: "Lora", Georgia, serif; font-weight: 400; font-size: 21px; color: var(--orange); line-height: 34px; text-decoration: underline; text-underline-offset: 5px; white-space: nowrap; }
  .section-title.big { font-size: 26px; }
  .section-title.dark { color: var(--ink); }
  .content p { margin-top: 18px; width: 1080px; }
  .narrow p, .narrow .ticks { width: 800px; }
  .ticks { list-style: none; margin-top: 12px; }
  .ticks li { color: var(--orange); padding-left: 34px; position: relative; margin-bottom: 8px; }
  .ticks svg { position: absolute; left: 0; top: 7px; }
  .quote-card { background: linear-gradient(160deg, #7b8894, #3c4652); }
  .quote-card.light { background: linear-gradient(160deg, #e9e4df, #bfb6ad); }
  .partner { left: 800px; top: 3380px; width: 360px; text-align: center; }
  .partner-name { display: flex; align-items: center; justify-content: center; gap: 12px; font-family: "Lora", Georgia, serif; font-weight: 700; font-size: 30px; color: var(--navy); line-height: 40px; }
  .partner-dot { width: 28px; height: 28px; border-radius: 50%; background: var(--orange); }
  .partner-tag { color: var(--orange); font-size: 15px; margin-top: 16px; }
  .details p { margin-top: 0; line-height: 58px; color: var(--orange); width: 700px; }

  /* footer */
  .footer { left: 0; top: 4110px; width: 1200px; height: 84px; background: var(--navy); color: var(--white); font-size: 16px; text-align: center; line-height: 84px; }
</style>
</head>
<body>

<header>
  <div class="abs brand"><span class="brand-dot"></span><span class="brand-name">Open Sky Living</span></div>
  <div class="abs contact">
    <svg width="30" height="22" viewBox="0 0 30 22" aria-hidden="true"><rect x="1" y="1" width="28" height="20" fill="none" stroke="#1f2a3c" stroke-width="2"/><path d="M1 1 L15 12 L29 1" fill="none" stroke="#1f2a3c" stroke-width="2"/></svg>
    <span>Email me: hello@openskyliving.co</span>
  </div>
</header>

<div class="abs hero-photo" role="img" aria-label="Two hands forming a heart shape against a glowing sunset sky"></div>
<svg class="abs hero-shapes" width="1200" height="1960" viewBox="0 0 1200 1960" aria-hidden="true">
  <path d="M0 140 L0 300 C 250 210 520 170 760 150 L0 140 Z" fill="#ffffff"/>
  <path d="M0 960 C 260 1140 640 1120 1200 880 L1200 1720 L0 1860 Z" fill="#1f2a3c"/>
  <path d="M0 1860 L1200 1720 L1200 1740 L0 1880 Z" fill="#e8861e"/>
  <path d="M0 1880 L1200 1740 L1200 1960 L0 1960 Z" fill="#ffffff"/>
</svg>

<section>
  <div class="abs portrait" role="img" aria-label="Portrait photo of Dana, the coach, wearing a blue cap"></div>
  <div class="abs welcome">
    <h1>Hello Friends!!</h1>
    <p>I am excited to (hopefully) add a little love to your in-box with this newsletter. I love connecting with moms and helping them find tools to make their lives happier, more intentional, and more fun and this is a new way to do that!</p>
    <p>If you don't know me well, I am a certified Boundless Paths Trainer and I lead coaching groups for moms. My Boundless Paths workshop and Bright Moms Circle have the goal of fostering connections between amazing women and empowering moms with tools to build lives they are enthusiastic about living, on purpose – and that will be the goal of this newsletter as well.</p>
    <p>I hope you find something useful and helpful and enjoy receiving this info (and if not, feel free to unsubscribe and my feelings will not be hurt! ☺)</p>
    <div class="signoff">With love, Dana</div>
  </div>
</section>

<main>
  <div class="abs content narrow" style="top:1940px;">
    <h2 class="section-title big">Building Happiness</h2>
    <p>I firmly believe that thinking about your happiness is important and that happiness itself is a worthwhile goal! If you think about all the things you focus on in your life and all the goals you set for yourself; all of those things are leading you toward feeling happier. Happiness, in the end, is the ultimate goal.</p>
    <p>Of course, what makes each person happy is totally different – and that's awesome and one part of what makes life fun and exciting! Many happiness experts and authors note that the key ingredients in our lives that will make us happier are pursuing 2 categories:</p>
    <ul class="ticks">
      <li><svg width="20" height="16" viewBox="0 0 20 16" aria-hidden="true"><path d="M2 8 L8 14 L18 2" fill="none" stroke="#e8861e" stroke-width="3"/></svg>Things that bring us pleasure (positive emotions) and</li>
      <li><svg width="20" height="16" viewBox="0 0 20 16" aria-hidden="true"><path d="M2 8 L8 14 L18 2" fill="none" stroke="#e8861e" stroke-width="3"/></svg>Things that bring us meaning &amp; fulfillment</li>
    </ul>
    <p>Give yourself a minute to think about (it's extra powerful if you write it down!) what makes YOU happy.</p>
  </div>
  <div class="abs quote-card light" style="left:900px; top:2048px; width:250px; height:230px;" role="img" aria-label="Quote card: happiness is found in the simplest of things"></div>
  <div class="abs quote-card" style="left:900px; top:2300px; width:250px; height:200px;" role="img" aria-label="Quote card: happiness is something you design for the present"></div>

  <div class="abs content" style="top:2520px;">
    <h2 class="section-title">What are things that make you feel happy / provide you with pleasure (little and big things)?</h2>
    <p>For me: joking &amp; laughing with my kids &amp; husband, petting with my dog, sitting with a soft blanket and a book, my first sip of coffee in the morning, walking in nature, traveling, scuba diving, exercise classes, making my friends laugh.</p>
  </div>

  <div class="abs content" style="top:2745px;">
    <h2 class="section-title">What are things that are meaningful to you / make you feel fulfilled (little and big things)?</h2>
    <p>For me: teaching Boundless Paths workshops, spending quality time with my family, making gratitude lists, volunteering, leading moms' coaching groups, making my kids breakfast.</p>
  </div>

  <div class="abs content" style="top:2965px;">
    <h2 class="section-title">How could you add more of those things that bring you happiness to your days?</h2>
    <h2 class="section-title" style="margin-top:22px;">Try to add 1 or 2 of those things per week and see how your happiness increases! You are worth it!</h2>
  </div>

  <div class="abs content" style="top:3160px;">
    <h2 class="section-title big dark">Empowering Books</h2>
    <p>I love to read uplifting, inspiring material. Each newsletter, I'll suggest a few books that I've enjoyed! "The Joy Ledger" by Marion Hale and "Bold and Bright: How to Quiet Your Doubts and Start Living a Fuller Life" by Tessa Lorne</p>
  </div>

  <div class="abs content" style="top:3390px;">
    <h2 class="section-title big dark">Upcoming Events:</h2>
    <p style="width:700px;">I lead a Boundless Paths Workshop 2-3 times per year. The next one is coming up in September/October. More details to come – but here is a little info…</p>
    <p style="margin-top:30px;">In September, the kids will be going back to school and you can spend time focusing on YOU. Let this be the year where you take time to focus on yourself so that you can feel amazing, focused, fulfilled, purposeful, and happier! Take the time to learn some simple tools to help you live a life you love, deliberately, instead of just juggling what comes at you and juggling your to-do list. In this workshop, you will be empowered to build a life you love.</p>
  </div>
  <div class="abs partner">
    <div class="partner-name"><span class="partner-dot"></span>Boundless Paths</div>
    <div class="partner-tag">Moms - Back to School, Back to You!</div>
  </div>

  <div class="abs content details" style="top:3750px;">
    <p>Dates: 3 morning workshop – September 27, October 4, October 11</p>
    <p>8:30 – 12:30</p>
    <p>Dana's home in Maple Ridge</p>
    <p>Interested? Email me: hello@openskyliving.co</p>
  </div>
  <div class="abs quote-card light" style="left:840px; top:3745px; width:320px; height:210px;" role="img" aria-label="Quote card about happiness from a well-known musician"></div>

  <div class="abs content" style="top:4005px;">
    <p style="margin-top:0; width:760px;">Enjoy the rest of Summer Break! Savor each amazing day! How can you add a little more HAPPY to your August?? Make the choice and do it!</p>
  </div>
</main>

<footer class="abs footer">© Copyright-2018 Open Sky Living All rights reserved</footer>

</body>
</html>
```